Fernbrook Vale Executive Development Workshop Series

* Had error in first version of MS Word doc and have re-uploaded - twelve subject areas, not nine *
I'd like a flyer to print to hand out and post on my website fernbrookvale.com to advertise a workshop series I'm launching. I'd like it to build strongly on the wonderful logo you did and Scottish theme...and to have the same "feel" as my website. fernbrookvale.com
It should be 8.5x11, single sided. Not sure if I should use full color glossy or two-color on nice paper. Regardless, I will most likely have it done on a color copier and will not put it on a printing press.
I have typed up a document with all the information in a MS Word file, but need you to lay it out in an aesthetically pleasing way. I have attached that MS Word file.
I am also attaching a handful of similar flyer documents from other non-competing coaches in my network. I think they all have their merits, but leave me under-whelmed.
I'm also attaching a picture of me and some pictures of Scotland my parents took about 10 years ago. I'm reluctantly open to stock photos, just not too obvious or hackneyed (if that word can be applied to pictures as well as expressions).
Lastly, this workshop series will be an ongoing thing, so I'd like to be able to make minor edits myself with things like new dates or topics.
Thank you!
Target Market(s)
Small business owners and emerging leaders with large companies
Colors
Designer to choose colors to be used in the design.
Requirements
Should not have
- Obviously stock photos

```html
<!DOCTYPE html>
<html lang="en">
<head>
<meta charset="utf-8">
<title>Fernbrook Vale Executive Development Workshop Series</title>
<link href="https://fonts.googleapis.com/css2?family=Cinzel:wght@400;700&family=Oswald:wght@300&family=Lato:wght@400;700&display=swap" rel="stylesheet">
<style>
  :root {
    --olive: #4f5a23;
    --olive-dark: #3b4419;
    --olive-light: #7a8545;
    --ink: #2f2f2f;
    --grey: #5a5a5a;
    --paper: #ffffff;
    --backdrop: #eceeed;
    --box: #e6e6e4;
  }
  * { box-sizing: border-box; margin: 0; padding: 0; }
  html, body { width: 1200px; height: 1200px; overflow: hidden; background: var(--backdrop); }
  body { position: relative; font-family: "Lato", sans-serif; color: var(--ink); }

  .flyer {
    position: absolute; left: 160px; top: 30px;
    width: 880px; height: 1140px;
    background: var(--paper);
    overflow: hidden;
    box-shadow: 0 8px 30px rgba(0,0,0,.18);
  }
  .flyer-art { position: absolute; inset: 0; }

  .brand {
    position: absolute; left: 500px; top: 52px; width: 300px;
    display: flex; align-items: center; gap: 10px; justify-content: center;
    font-family: "Cinzel", serif; font-weight: 400; font-size: 24px;
    color: #f3f1e6; letter-spacing: 1px;
  }
  .brand-dot { width: 12px; height: 12px; border-radius: 50%; background: #f3f1e6; }

  .headline { position: absolute; left: 465px; top: 222px; width: 400px; text-align: center; white-space: nowrap; }
  .headline-purpose {
    font-family: "Oswald", sans-serif; font-weight: 300; font-size: 32px;
    color: var(--olive-dark); letter-spacing: 1px; line-height: 1.1;
  }
  .headline-path {
    font-family: "Cinzel", serif; font-weight: 700; font-size: 36px;
    color: var(--ink); line-height: 1.15; letter-spacing: 1px;
  }

  .photo-circle { position: absolute; border-radius: 50%; border: 6px solid var(--olive); }
  .photo-village { left: 708px; top: 335px; width: 160px; height: 160px;
    background: linear-gradient(160deg, #b9c7cf 0%, #8c9a6d 45%, #7b5a3a 100%); }
  .photo-pub { left: 708px; top: 505px; width: 160px; height: 160px;
    background: linear-gradient(160deg, #6d6a63 0%, #b4382b 55%, #7c2a20 100%); }

  .content { position: absolute; left: 36px; top: 385px; width: 650px; }
  .pill {
    display: inline-block; background: var(--olive); color: #fff;
    font-family: "Cinzel", serif; font-weight: 700; font-size: 13px;
    padding: 4px 18px; border-radius: 14px; letter-spacing: .3px; white-space: nowrap;
  }
  .intro { font-size: 11px; line-height: 1.32; color: var(--grey); margin-top: 6px; }
  .intro + .intro { margin-top: 4px; }
  .topics { list-style: none; margin-top: 4px; font-size: 10.5px; line-height: 1.34; color: var(--grey); }
  .topics b { color: var(--olive); }
  .includes { margin-top: 8px; }
  .bullets { list-style: none; margin-top: 6px; width: 600px; font-size: 10.5px; line-height: 1.32; color: var(--grey); }
  .bullets li { position: relative; padding-left: 16px; margin-bottom: 3px; }
  .bullets li::before { content: "\27A4"; position: absolute; left: 0; top: 0; color: var(--olive); font-size: 9px; }
  .bullets b { color: var(--olive); }
  .bullets .and { font-weight: 700; padding-left: 16px; }
  .bullets .and::before { content: none; }

  .register {
    margin-top: 6px; width: 580px; background: linear-gradient(180deg, #f4f4f2, var(--box));
    border: 2px solid var(--olive); border-radius: 16px; padding: 6px 14px;
    font-size: 10.5px; line-height: 1.38; color: var(--grey);
  }
  .register b { color: var(--olive-dark); }
  .price { display: inline-block; background: var(--olive); color: #fff; font-weight: 700; padding: 0 8px; border-radius: 8px; }

  .portrait {
    position: absolute; left: 690px; top: 690px; width: 190px; height: 280px;
    background: linear-gradient(180deg, #e9ecef 0%, #cfd3d6 40%, #7e705f 75%, #5e5246 100%);
  }
  .photo-coast { left: 640px; top: 925px; width: 150px; height: 150px;
    background: linear-gradient(180deg, #c9ced2 0%, #9aa3a8 45%, #4f5a3a 70%, #3a3d3a 100%); }

  .contact { position: absolute; left: 40px; top: 1028px; list-style: none; color: #fff; font-size: 15px; line-height: 1.3; }
  .contact li { display: flex; align-items: flex-start; gap: 10px; }
  .contact svg { width: 14px; height: 14px; margin-top: 3px; flex: none; }
</style>
</head>
<body>
<main class="flyer">
  <svg class="flyer-art" viewBox="0 0 880 1140" width="880" height="1140">
    <defs>
      <linearGradient id="ruinGreen" x1="0" y1="0" x2="1" y2="1">
        <stop offset="0" stop-color="#c7d2c9"/>
        <stop offset=".35" stop-color="#7fa43c"/>
        <stop offset=".7" stop-color="#5d8a2a"/>
        <stop offset="1" stop-color="#8d8a7a"/>
      </linearGradient>
      <linearGradient id="bandGrad" x1="0" y1="0" x2="1" y2="0">
        <stop offset="0" stop-color="#3b4419"/>
        <stop offset="1" stop-color="#4f5a23"/>
      </linearGradient>
    </defs>
    <path role="img" aria-label="Photo of grassy stone ruins on a Scottish coast" d="M0,0 H325 C318,150 350,290 392,372 L0,372 Z" fill="url(#ruinGreen)"/>
    <path d="M342,0 H880 V150 C660,150 490,160 438,250 C420,285 410,330 404,368 C370,290 346,160 342,0 Z" fill="url(#bandGrad)"/>
    <path d="M0,1140 V1015 C250,960 560,1010 880,940 V1140 Z" fill="var(--olive)"/>
    <path d="M0,1004 C250,949 560,999 880,929" fill="none" stroke="var(--olive-light)" stroke-width="5"/>
  </svg>

  <div class="brand"><span class="brand-dot"></span>Fernbrook Vale</div>

  <header class="headline">
    <p class="headline-purpose">CLARITY OF PURPOSE</p>
    <h1 class="headline-path">CLARITY OF PATH</h1>
  </header>

  <div class="photo-circle photo-village" role="img" aria-label="Photo of a Highland village with long-haired cattle"></div>
  <div class="photo-circle photo-pub" role="img" aria-label="Photo of a red-fronted pub with a small dog statue"></div>

  <section class="content">
    <h2 class="pill">Fernbrook Vale Executive Development Workshop Series – First Thursdays</h2>
    <p class="intro">A positive, fresh, results-driven approach for businesses to increase profits by building confidence, command and control in owners and executives. We will use proven leadership and business strategies to improve work-life balance, buy-in, and company value. Here’s your opportunity to meet with other like-minded business owners and executives once a month in a private and confidential setting.</p>
    <p class="intro">We’ve got twelve subject areas planned, and while they are all powerful, we will shift from high-level strategy topics to “where the rubber meets the road” topics.</p>
    <ul class="topics">
      <li><b>Sep 7</b> – My Company Owns Me – What a CEO should and should not do</li>
      <li><b>Oct 5</b> – Taking Vision / Mission / Values Down To The Molecular Level Of Your Company</li>
      <li><b>Nov 2</b> – People Problems – The biggest waste of time and money for every small business</li>
      <li><b>Dec 7</b> – Value Delivery Systems – Re-think everything you think you know about creating value</li>
      <li><b>Jan 4, 2018</b> – Rally Your Team Around A Goal – How to create a meaningful company goal and rally the troops around it</li>
      <li><b>Feb 1</b> – Building Your Executive Leadership Team – You can’t succeed without one</li>
      <li><b>Mar 1</b> – Improve Your Outside Sales Efforts – Help your sales force to be busy AND successful</li>
      <li><b>Apr 5</b> – Every Brain In The Game – Engage your team and build a strong culture</li>
      <li><b>May 3</b> – Repeatable Processes – Coach your employees how to get predictable results every time</li>
      <li><b>Jun 7</b> – Finding and Filling Profit Holes – Most small businesses waste more money than they profit</li>
      <li><b>*Jul 12</b> – Put Your Payroll On A Diet – Why waste happens, what to do about it and how it helps everyone</li>
      <li><b>Aug 2</b> – Truly, How Effective Are You With This Whole “Leadership” Thing?</li>
    </ul>

    <h2 class="pill includes">Each Month of This Monthly Workshop Series Includes:</h2>
    <ul class="bullets">
      <li>3-Hour Intensive Workshop - High-energy, creative sessions with engaging and relevant business topics, peer group advisory board (master mind), and networking <b>(9am – 12pm, dates above)</b></li>
      <li class="and">AND</li>
      <li><b>90-minute</b> one-on-one coaching session – to help you absorb and apply the revelations from the group sessions to your own business (mutually scheduled)</li>
      <li>Participation and trust is vital to your investment; no holding back. Due to the confidential nature of the intensive workshops, all participants will sign a confidentiality agreement. Additionally, we will only allow one company per industry to be represented.</li>
    </ul>

    <div class="register">
      <p><b>To register, go to fernbrookvale.com/exec-dev and click the registration link</b></p>
      <p><span class="price">$395/month or $295/month</span> with a <b>6-month</b> or <b>greater commitment</b></p>
      <p>All monthly Intensive Workshops will be <b>9am – 12pm</b> on the dates above at Millhouse Coworking at <b>218 Larkspur Lane</b>, Ashford, <b>NC 27999</b></p>
      <p>All one-on-one coaching sessions will be mutually scheduled with <b>Colin Maddox</b> once you have registered</p>
    </div>
  </section>

  <div class="portrait" role="img" aria-label="Portrait photo of coach Colin Maddox in a tweed jacket"></div>
  <div class="photo-circle photo-coast" role="img" aria-label="Photo of a rocky Scottish coastline under grey sky"></div>

  <ul class="contact">
    <li><svg viewBox="0 0 16 16"><path d="M4 1 L6.5 1 L7.5 4.5 L5.8 5.8 C6.6 7.8 8.2 9.4 10.2 10.2 L11.5 8.5 L15 9.5 L15 12 C15 13.7 13.7 15 12 15 C6 15 1 10 1 4 C1 2.3 2.3 1 4 1 Z" fill="#fff"/></svg>(555)014-2290</li>
    <li><svg viewBox="0 0 16 16"><rect x="1" y="3" width="14" height="10" rx="1" fill="#fff"/><path d="M1.5 3.5 L8 9 L14.5 3.5" fill="none" stroke="var(--olive)" stroke-width="1.4"/></svg>colin@fernbrookvale.com</li>
    <li><svg viewBox="0 0 16 16" fill="none" stroke="#fff" stroke-width="1.4"><circle cx="8" cy="8" r="6.5"/><ellipse cx="8" cy="8" rx="3" ry="6.5"/><path d="M1.5 8 H14.5 M2.5 4.5 H13.5 M2.5 11.5 H13.5"/></svg>www.fernbrookvale.com</li>
    <li><svg viewBox="0 0 16 16"><path d="M8 1 C5.2 1 3.2 3 3.2 5.7 C3.2 9.2 8 14.5 8 14.5 C8 14.5 12.8 9.2 12.8 5.7 C12.8 3 10.8 1 8 1 Z" fill="#fff"/><circle cx="8" cy="5.8" r="1.8" fill="var(--olive)"/></svg><span>218 Larkspur Lane<br>Ashford, NC 27999</span></li>
  </ul>
</main>
</body>
</html>
```